Personal Card: Make it roar!

Hello to all designers,
Hope you're having a nice day/evening! Let's cut to the chase. I would like a modern, beautiful and professional personal business card; with a vector-art of a lion. I'd like the lion to be Blood Red. On a black background. I'm a Filipino, and would love to have my country's flag incorporated into the design. Id like the stars of my flag to be used in your designs if possible. The texts I want on the card are only my name, number, and email address. Colour of my name should be White, and my details Silver. The size and font should be simple and professional, you're in charge of that! The placements of the lion and my details will be yours to decide.

At the back of the card, I would like just the words "Thank You" (Silver) on a Black Background. Right on the center.

To summarise, my requirements are:
- Blood Red: Front Face of Lion, Vector-Art
- Black: Background
- Yellow: Three Stars used in the design
- White: Bartholomew Sr Pelaez
- Silver: Number & Email (Where appropriate)
- Back of the card (Center). Silver: "Thank You"
- Please DON'T use the colour blue.

It's all about the Lion. Images you'll find attached are some images of Lions' faces which I particularly want to be captured and put onto the card. Convert it into a vector-art. A vector-art Lion. PLEASE use the images attached for inspiration only! Do not use it on your designs. Thank you very much for your time.

Good luck!

Bart

Hello Desginers, Please use Blood Red for the colour red in your designs:HEX: 8A0707RGB: 138,7,7Thank you,Bart Added Saturday, March 12, 2016

Target Market(s)

Potential Connections

Industry/Entity Type

It Professional

Contact Information for Business Card

Name: Bartholomew Sr Pelaez
Email: bartpelaez@zentomail.example
Number: 07391628047

Requirements
Must have
• Modern, Professional & Simple
• (Blood Red HEX: 8A0707, RGB: 138,7,7) Lion (Vector-style art)
• (Black) Background
• (White) My Name
• (Silver) My Details
• Back of card: "Thank You" in Silver. Font size should be small/medium.
• Only colours that should be used are Red, Black, Yellow and White/Silver
Nice to have
• - Use of 3 Yellow stars on the design
Should not have
• - Please avoid using any other colours apart from those specified.

```html
<!DOCTYPE html>
<html lang="en">
<head>
<meta charset="utf-8">
<title>Bartholomew Sr Pelaez — Personal Card</title>
<link rel="stylesheet" href="https://fonts.googleapis.com/css2?family=Bodoni+Moda:wght@700&family=Cinzel:wght@400;500&display=swap">
<style>
  :root {
    --backdrop: #cfcfcf;
    --card-black: #0b0b0b;
    --brush-red: #8a2424;
    --brush-red-deep: #6e1414;
    --mane-light: #ececec;
    --mane-mid: #b9b9b9;
    --mane-dark: #3a3a3a;
    --star-yellow: #f2cf2b;
    --name-white: #ffffff;
    --detail-silver: #bdbdbd;
    --silver-light: #e6e6e6;
    --silver-dark: #8f8f8f;
  }
  html, body {
    margin: 0;
    padding: 0;
    width: 1200px;
    height: 1098px;
    overflow: hidden;
    background: var(--backdrop);
  }
  .sheet { position: relative; width: 1200px; height: 1098px; }
  .card {
    position: absolute;
    left: 220px;
    width: 760px;
    height: 490px;
    background: var(--card-black);
    box-shadow: 0 6px 18px rgba(0,0,0,0.25);
    overflow: hidden;
  }
  .card--back { top: 39px; }
  .card--front { top: 569px; }

  .thank-you {
    position: absolute;
    inset: 0;
    display: flex;
    align-items: center;
    justify-content: center;
    margin: 0;
    font-family: "Cinzel", "Times New Roman", serif;
    font-weight: 500;
    font-size: 38px;
    letter-spacing: 0.1em;
    background: linear-gradient(180deg, var(--silver-light), var(--silver-dark));
    -webkit-background-clip: text;
    background-clip: text;
    color: transparent;
  }

  /* red brush blocks behind the emblem */
  .brush {
    position: absolute;
    background: linear-gradient(160deg, var(--brush-red), var(--brush-red-deep));
  }
  .brush--left   { left: 212px; top: 96px;  width: 74px;  height: 62px;  transform: rotate(-8deg); }
  .brush--top    { left: 404px; top: 62px;  width: 96px;  height: 82px;  transform: rotate(10deg); }
  .brush--right  { left: 468px; top: 150px; width: 72px;  height: 160px; transform: rotate(6deg); }
  .brush--bottom { left: 346px; top: 286px; width: 86px;  height: 64px;  transform: rotate(8deg); }

  .lion-art {
    position: absolute;
    left: 246px;
    top: 66px;
    width: 262px;
    height: 262px;
    border-radius: 48% 52% 44% 46% / 50% 50% 50% 50%;
    background: radial-gradient(ellipse 60% 65% at 50% 52%, var(--mane-dark) 0%, var(--mane-mid) 55%, var(--mane-light) 100%);
  }

  .star { position: absolute; width: 48px; height: 48px; }
  .star path { fill: var(--star-yellow); }
  .star--left   { left: 206px; top: 196px; }
  .star--right  { left: 530px; top: 132px; }
  .star--bottom { left: 365px; top: 298px; }

  .identity {
    position: absolute;
    left: 0;
    right: 0;
    top: 350px;
    text-align: center;
  }
  .identity__block { display: inline-block; text-align: left; }
  .holder-name {
    margin: 0;
    font-family: "Bodoni Moda", "Times New Roman", serif;
    font-weight: 700;
    font-size: 30px;
    line-height: 1.2;
    letter-spacing: 0.22em;
    color: var(--name-white);
    text-transform: uppercase;
  }
  .details {
    display: flex;
    justify-content: space-between;
    align-items: flex-start;
    gap: 24px;
    margin-top: 6px;
  }
  .detail {
    margin: 0;
    font-family: "Cinzel", "Times New Roman", serif;
    font-weight: 400;
    font-size: 18px;
    letter-spacing: 0.08em;
    color: var(--detail-silver);
    white-space: nowrap;
  }
  .detail--email { margin-top: 22px; text-transform: uppercase; font-size: 17px; }
</style>
</head>
<body>
<main class="sheet">
  <section class="card card--back" aria-label="Card back">
    <p class="thank-you">THANK YOU</p>
  </section>

  <section class="card card--front" aria-label="Card front">
    <div class="brush brush--left"></div>
    <div class="brush brush--top"></div>
    <div class="brush brush--right"></div>
    <div class="brush brush--bottom"></div>

    <div class="lion-art" role="img" aria-label="Black and white patterned vector lion head, front view"></div>

    <svg class="star star--left" viewBox="0 0 100 100" aria-hidden="true">
      <path d="M50 4 61 38 97 38 68 59 79 94 50 73 21 94 32 59 3 38 39 38Z"/>
    </svg>
    <svg class="star star--right" viewBox="0 0 100 100" aria-hidden="true">
      <path d="M50 4 61 38 97 38 68 59 79 94 50 73 21 94 32 59 3 38 39 38Z"/>
    </svg>
    <svg class="star star--bottom" viewBox="0 0 100 100" aria-hidden="true">
      <path d="M50 4 61 38 97 38 68 59 79 94 50 73 21 94 32 59 3 38 39 38Z"/>
    </svg>

    <div class="identity">
      <div class="identity__block">
        <h1 class="holder-name">Bartholomew Sr Pelaez</h1>
        <div class="details">
          <p class="detail detail--phone">07391628047</p>
          <p class="detail detail--email">bartpelaez@zentomail.example</p>
        </div>
      </div>
    </div>
  </section>
</main>
</body>
</html>
```